Bramwell Resources Ltd. - Refreshed business card challenge

A revised, refreshed business card design for my oil and gas company using my existing logo. Feel free to be as creative as you like!

Target Market(s)

bankers, lawyers

Industry/Entity Type

Oil And Gas Exploration

Contact Information for Business Card

See the "Must Haves" section

Font styles to use
Serif
Sans Serif

Colors

Designer to choose colors to be used in the design.

Requirements
Must have
• Existing business logo, name, title, email, phone number, business address
• Neil Hadley, CA, CPA
• Vice President Finance & Chief Financial Officer
• nhadley@bramwellresources-mail.com
• office: (587)555-0142
• cell: (403)555-0187
• 1400, 815 4 Street S.W.
• Calgary, AB
• T2P 4K8
Should not have
• Should not be plain and boring.

```html
<!DOCTYPE html>
<html lang="en">
<head>
<meta charset="utf-8">
<title>Bramwell Resources – Business Card</title>
<link href="https://fonts.googleapis.com/css2?family=Arimo:wght@400;700&display=swap" rel="stylesheet">
<style>
  :root {
    --page-bg: #2e2e2e;
    --forest: #0f4d34;
    --forest-light: #1b6446;
    --card-white: #f7f7f7;
    --ink-green: #0f5a3a;
    --ink-brown: #5a2c12;
    --tree-brown: #6b3a1c;
  }
  * { margin: 0; padding: 0; box-sizing: border-box; }
  html, body { width: 1200px; height: 900px; overflow: hidden; }
  body {
    background: var(--page-bg);
    font-family: "Arimo", Arial, sans-serif;
    display: flex;
    align-items: center;
    justify-content: center;
    gap: 70px;
  }
  .card {
    position: relative;
    width: 380px;
    height: 660px;
    border-radius: 26px;
    overflow: hidden;
  }
  .card-front {
    background: linear-gradient(160deg, var(--forest-light), var(--forest) 55%);
  }
  .front-decoration {
    position: absolute;
    right: 0;
    top: 0;
    width: 170px;
    height: 100%;
    background: linear-gradient(90deg, rgba(255,255,255,0) 0%, rgba(255,255,255,0.07) 60%, rgba(255,255,255,0.03) 100%);
  }
  .front-brand {
    position: absolute;
    left: 36px;
    top: 180px;
    color: #fff;
    font-weight: 700;
    font-size: 38px;
    line-height: 1.05;
    letter-spacing: -0.5px;
  }
  .card-back {
    background: linear-gradient(170deg, #ffffff, var(--card-white) 60%, #e9e9e9);
  }
  .back-decoration {
    position: absolute;
    right: 0;
    top: 0;
    width: 140px;
    height: 420px;
    background: linear-gradient(90deg, rgba(0,0,0,0) 0%, rgba(0,0,0,0.04) 70%, rgba(0,0,0,0.02) 100%);
  }
  .contact {
    position: absolute;
    right: 28px;
    top: 34px;
    text-align: right;
    font-weight: 700;
    font-size: 15px;
    line-height: 1.28;
    color: var(--ink-brown);
  }
  .contact .name {
    color: var(--ink-green);
    font-size: 21px;
    margin-bottom: 2px;
  }
  .contact .block { margin-top: 18px; }
  .contact .phone { color: var(--ink-green); }
  .tree-art {
    position: absolute;
    left: 30px;
    bottom: 40px;
    width: 120px;
    height: 270px;
    border-radius: 50% 50% 10px 10px / 30% 30% 10px 10px;
    background: linear-gradient(180deg, #2f7a4d 0%, #1f6640 70%, var(--tree-brown) 100%);
  }
  .back-brand {
    position: absolute;
    right: 28px;
    bottom: 82px;
    text-align: right;
    color: var(--ink-green);
    font-weight: 700;
    font-size: 32px;
    line-height: 1.05;
    letter-spacing: -0.5px;
  }
</style>
</head>
<body>
  <div class="card card-front">
    <div class="front-decoration" role="img" aria-label="Faint tall conifer tree silhouette"></div>
    <div class="front-brand">Bramwell<br>Resources</div>
  </div>

  <div class="card card-back">
    <div class="back-decoration" role="img" aria-label="Faint conifer tree silhouette"></div>
    <div class="contact">
      <div class="name">Neil Hadley, CA, CPA</div>
      <div>Vice President</div>
      <div>Finance &amp; Chief Financial Officer</div>
      <div class="block phone">
        <div>office: (587) 555 0142</div>
        <div>cell: (403) 555 0187</div>
      </div>
      <div class="block">
        <div>nhadley@bramwellresources-mail.com</div>
        <div>www.bramwellresources-mail.com</div>
      </div>
      <div class="block">
        <div>1400, 815 4 Street S.W.</div>
        <div>Calgary, AB</div>
        <div>T2P 4K8</div>
      </div>
    </div>
    <div class="tree-art" role="img" aria-label="Illustration of a tall green conifer tree with brown trunk and small trees at its base"></div>
    <div class="back-brand">Bramwell<br>Resources</div>
  </div>
</body>
</html>
```